Business Card

I would like a business card with a picture of my husband and I that is unique and professional.

Industry/Entity Type

Business

Font styles to use
Serif

```html
<!DOCTYPE html>
<html lang="en">
<head>
<meta charset="utf-8">
<title>Dalton Leadership Development – Business Card</title>
<link rel="stylesheet" href="https://fonts.googleapis.com/css2?family=Didact+Gothic&display=swap">
<style>
  :root {
    --stage: #e7e7e7;
    --card-white: #ffffff;
    --ink: #1d1d1d;
    --accent: #f2a93b;
    --band-dark: #4a4a4c;
    --band-mid: #5d5d60;
    --back-dark: #4b4b4d;
    --back-light: #6a6a6d;
    --faint: rgba(200, 200, 200, 0.35);
    --photo-dark: #5b5b60;
    --photo-light: #b9b3ad;
  }
  * { margin: 0; padding: 0; box-sizing: border-box; }
  html, body { width: 1200px; height: 900px; overflow: hidden; }
  body {
    background: var(--stage);
    font-family: "Didact Gothic", "Century Gothic", sans-serif;
    position: relative;
  }
  .card {
    position: absolute;
    top: 296px;
    width: 540px;
    height: 308px;
    border-radius: 26px;
    overflow: hidden;
  }
  .card-front { left: 40px; background: var(--card-white); }
  .card-back {
    left: 620px;
    background: linear-gradient(135deg, var(--back-light), var(--back-dark));
  }

  /* brand block */
  .brand {
    position: absolute;
    left: 34px;
    top: 34px;
    display: flex;
    align-items: center;
    gap: 10px;
  }
  .brand-dot {
    width: 30px; height: 30px;
    border-radius: 50%;
    background: var(--band-dark);
  }
  .brand-name {
    font-size: 15px;
    color: var(--ink);
    letter-spacing: 0.5px;
  }
  .brand-sub {
    position: absolute;
    left: 34px;
    top: 80px;
    font-size: 9px;
    letter-spacing: 0.8px;
    color: var(--ink);
    text-transform: uppercase;
  }

  .watermark-name {
    position: absolute;
    left: 270px;
    top: 70px;
    font-size: 54px;
    color: #f1f1f1;
  }

  .photo {
    position: absolute;
    left: 336px;
    top: 72px;
    width: 162px;
    height: 186px;
    background: linear-gradient(160deg, var(--photo-light), var(--photo-dark));
    border-radius: 6px 6px 0 0;
  }

  .contact-name {
    position: absolute;
    left: 24px;
    top: 150px;
    font-size: 19px;
    color: var(--accent);
  }
  .contact-title {
    position: absolute;
    left: 24px;
    top: 176px;
    font-size: 14px;
    color: var(--ink);
  }
  .contact-list {
    position: absolute;
    left: 24px;
    top: 212px;
    list-style: none;
    font-size: 15px;
    color: var(--ink);
  }
  .contact-list li {
    display: flex;
    align-items: center;
    gap: 8px;
    height: 20px;
  }
  .contact-list svg { width: 14px; height: 14px; fill: var(--accent); }

  .accent-line {
    position: absolute;
    left: 0; right: 0;
    top: 258px;
    height: 4px;
    background: var(--accent);
  }
  .footer-band {
    position: absolute;
    left: 0; right: 0; bottom: 0;
    height: 46px;
    background: linear-gradient(180deg, var(--band-mid), var(--band-dark));
  }

  .back-mark {
    position: absolute;
    left: 0; right: 0; top: 112px;
    display: flex;
    justify-content: center;
    align-items: center;
    gap: 14px;
  }
  .back-mark .brand-dot {
    width: 56px; height: 56px;
    background: var(--faint);
  }
  .back-mark .brand-name {
    font-size: 56px;
    color: var(--faint);
  }
</style>
</head>
<body>
  <section class="card card-front" aria-label="Business card front">
    <div class="watermark-name" aria-hidden="true">Dalton</div>

    <div class="brand">
      <span class="brand-dot"></span>
      <span class="brand-name">Dalton</span>
    </div>
    <div class="brand-sub">Dalton Leadership Development</div>

    <div class="photo" role="img" aria-label="Portrait photo of the couple in grey suits"></div>

    <h1 class="contact-name">Marisa Dalton</h1>
    <p class="contact-title">Professional Mentorship Strategist</p>
    <ul class="contact-list">
      <li>
        <svg viewBox="0 0 24 24" aria-hidden="true"><path d="M6.6 10.8a15.1 15.1 0 0 0 6.6 6.6l2.2-2.2c.3-.3.7-.4 1-.2 1.1.4 2.3.6 3.6.6.6 0 1 .4 1 1V20c0 .6-.4 1-1 1A17 17 0 0 1 3 4c0-.6.4-1 1-1h3.5c.6 0 1 .4 1 1 0 1.3.2 2.5.6 3.6.1.3 0 .7-.2 1z"/></svg>
        312-555-0148
      </li>
      <li>
        <svg viewBox="0 0 24 24" aria-hidden="true"><path d="M2 5h20v14H2zm2 2v.5l8 5 8-5V7z"/></svg>
        MarisaDalton@example.com
      </li>
    </ul>

    <div class="accent-line"></div>
    <div class="footer-band"></div>
  </section>

  <section class="card card-back" aria-label="Business card back">
    <div class="back-mark">
      <span class="brand-dot"></span>
      <span class="brand-name">Dalton</span>
    </div>
  </section>
</body>
</html>
```